Home care support

Design a a great and dynamic website for a healthcare business. Our business will be involved in providing care at home for people with disability and the elderly. Below is a link that I found for a company offering similar services in the US. I am looking for something like this .
I have my files - the latest project in here in through through Pixelmarket
Sample site : https://cedarbrookassistedliving.com/
Target Market(s)
people with disability and elderly seniors who need home care support
Industry/Entity Type
Health
Coding
Coded - Design and coding required
Number of Pages Required
5+ page
Requirements
Must have
- inspirational pictures and designed with the themed logo (files attached)
Nice to have
- This is my sample and should look like this : https://cedarbrookassistedliving.com/

```html
<!DOCTYPE html>
<html lang="en">
<head>
<meta charset="utf-8">
<title>Maplecrest Home Care</title>
<link href="https://fonts.googleapis.com/css2?family=Libre+Baskerville:wght@700&family=Montserrat:ital,wght@0,400;0,500;0,600;0,700;1,400&display=swap" rel="stylesheet">
<style>
:root{
  --blue:#1769a3;
  --blue-dark:#0f5585;
  --green:#5b9a3a;
  --ink:#1f1f1f;
  --text:#555;
  --dark:#262626;
  --dark-2:#3e4142;
  --light:#f3f4f6;
  --white:#fff;
}
*{box-sizing:border-box;margin:0;padding:0}
html,body{width:1200px;height:4296px;overflow:hidden}
body{position:relative;font-family:"Montserrat",sans-serif;color:var(--text);background:var(--white)}
.abs{position:absolute}
.serif{font-family:"Libre Baskerville",serif;font-weight:700;color:var(--ink);text-transform:uppercase}
.btn{position:absolute;display:flex;align-items:center;justify-content:center;gap:12px;font-weight:700;font-size:14px;letter-spacing:1px;color:#fff;text-transform:uppercase}
.btn .dot{width:22px;height:22px;border:2px solid #fff;border-radius:50%}
.btn.green{background:var(--green)}
.btn.blue{background:var(--blue)}
/* header */
.topbar{left:638px;top:0;width:562px;height:37px;background:var(--blue);clip-path:polygon(12px 0,100% 0,100% 100%,0 100%);color:#fff;font-size:15px;display:flex;align-items:center;gap:30px;padding-left:30px}
.topbar span{display:flex;align-items:center;gap:10px}
.topbar .sep{width:1px;height:18px;background:rgba(255,255,255,.5)}
.brand{left:92px;top:28px;display:flex;align-items:center;gap:12px}
.brand .mark{width:60px;height:60px;border-radius:50%;background:var(--blue)}
.brand .name{font-family:"Libre Baskerville",serif;font-weight:700;font-size:22px;color:var(--blue);line-height:1.1}
.nav{left:584px;top:64px;display:flex;gap:30px;font-size:15px;font-weight:600;color:#333}
.nav .active{color:var(--blue);position:relative}
.nav .active:after{content:"";position:absolute;left:8px;right:8px;top:36px;height:3px;background:var(--blue)}
.search{left:1070px;top:57px;width:37px;height:37px;border-radius:50%;background:var(--green)}
/* hero */
.hero{left:0;top:112px;width:1200px;height:590px;background:linear-gradient(90deg,#2a2a2a 0%,#4a4a4a 40%,#7a7c80 70%,#9aa0a6 100%)}
.hero h1{position:absolute;left:92px;top:122px;font-size:52px;line-height:1.22;color:#fff}
.hero h1 em{font-style:normal;color:var(--green)}
.hero .sub{position:absolute;left:94px;top:323px;font-size:18px;letter-spacing:2px;font-weight:600;color:#fff}
.arrow-side{position:absolute;width:37px;height:70px;background:rgba(60,60,60,.8);color:#fff;display:flex;align-items:center;justify-content:center;font-size:18px}
/* about */
.about-art{left:92px;top:750px;width:475px;height:467px;border-radius:50%;background:radial-gradient(circle,#fff 50%,#ececec 51%,#f6f6f6 75%,#fff 76%);display:flex;align-items:center;justify-content:center}
.about-art .core{width:310px;height:310px;border-radius:50%;border:14px solid var(--blue);display:flex;align-items:center;justify-content:center;font-family:"Libre Baskerville",serif;font-weight:700;font-size:30px;color:var(--blue);text-align:center;line-height:1.3}
.eyebrow{font-size:17px;font-weight:600;color:var(--blue);letter-spacing:1.5px;display:flex;align-items:center;gap:12px}
.eyebrow:after{content:"";width:62px;height:1px;background:var(--green)}
.body{font-size:17px;line-height:33px}
/* features */
.feature{position:absolute;top:1330px;width:310px;text-align:center}
.feature .icon{width:148px;height:148px;margin:0 auto;border-radius:50%;border:6px solid var(--green);border-bottom-color:transparent;display:flex;align-items:center;justify-content:center}
.feature .icon i{width:112px;height:112px;border-radius:50%;background:var(--blue);display:flex;align-items:center;justify-content:center}
.feature h3{font-size:20px;line-height:29px;margin-top:14px}
.feature p{font-size:17px;line-height:33px;margin-top:8px}
/* services */
.services-bg{left:0;top:1730px;width:1200px;height:840px;background:linear-gradient(180deg,#e9ebef 0%,#f2f3f5 55%,#fff 100%)}
.services-photo{left:0;top:1730px;width:380px;height:470px;background:linear-gradient(120deg,#b7a08a,#dcd6d2 60%,rgba(240,241,243,0))}
.center{text-align:center;left:0;width:1200px}
.card{position:absolute;top:1955px;width:325px;height:470px;background:#fff;box-shadow:0 4px 18px rgba(0,0,0,.08)}
.card .ph{height:212px}
.card h3{font-size:20px;margin:40px 0 0 25px}
.card p{font-size:17px;line-height:33px;margin:12px 25px 0}
.card .more{position:absolute;left:25px;top:390px;width:142px;height:45px;border:2px solid var(--blue);color:var(--blue);font-weight:700;font-size:14px;letter-spacing:1px;display:flex;align-items:center;justify-content:center}
.green-arrow{position:absolute;width:37px;height:70px;background:var(--green);color:#fff;display:flex;align-items:center;justify-content:center;font-size:18px}
/* testimonials */
.quote-pill{left:433px;top:2847px;width:607px;height:256px;background:var(--dark-2);border-radius:0 128px 128px 0}
.quote-text{left:532px;top:2872px;width:470px;font-style:italic;font-size:17px;line-height:33px;color:#fff}
.stars{display:flex;gap:5px;margin-top:4px}
/* contact */
.contact{left:0;top:3237px;width:1200px;height:620px;background:linear-gradient(135deg,#1a6ea8,#125b8d 60%,#1a6aa0)}
.field{position:absolute;background:#fff;font-size:15px;color:#666;padding:14px 18px}
/* footer */
.footer{left:0;top:3780px;width:1200px;height:516px;background:var(--dark)}
.footer h4{font-size:21px;color:#fff}
.footer .links{font-size:17px;line-height:39px;color:#ddd}
.ci{display:flex;gap:18px;align-items:flex-start;margin-bottom:22px;color:#ddd;font-size:17px;line-height:23px}
.ci .c{flex:none;width:40px;height:40px;border-radius:50%;background:var(--green);display:flex;align-items:center;justify-content:center}
.social{width:40px;height:40px;border-radius:50%;border:1px solid #777}
</style>
</head>
<body>

<!-- header -->
<div class="abs topbar">
  <span><svg width="16" height="16" viewBox="0 0 24 24" fill="#fff"><path d="M6.6 10.8a15 15 0 0 0 6.6 6.6l2.2-2.2c.3-.3.7-.4 1-.2 1.1.4 2.3.6 3.6.6.6 0 1 .4 1 1V20c0 .6-.4 1-1 1A17 17 0 0 1 3 4c0-.6.4-1 1-1h3.5c.6 0 1 .4 1 1 0 1.3.2 2.5.6 3.6.1.3 0 .7-.2 1z"/></svg>555-218-4630</span>
  <span class="sep"></span>
  <span><svg width="16" height="14" viewBox="0 0 24 20" fill="#fff"><rect x="1" y="2" width="22" height="16" rx="2"/><path d="M2 4l10 7 10-7" stroke="#1769a3" stroke-width="2" fill="none"/></svg>info@maplecresthomecare.com</span>
</div>
<div class="abs brand"><span class="mark"></span><span class="name">MAPLECREST<br><span style="font-size:11px;letter-spacing:5px;font-family:Montserrat,sans-serif;font-weight:500;color:var(--blue)">HOME CARE</span></span></div>
<nav class="abs nav"><span class="active">HOME</span><span>ABOUT</span><span>SERVICES</span><span>RESOURCES</span><span>CONTACT</span></nav>
<div class="abs search"><svg width="37" height="37" viewBox="0 0 37 37"><circle cx="17" cy="17" r="6" stroke="#fff" stroke-width="2" fill="none"/><line x1="21.5" y1="21.5" x2="25" y2="25" stroke="#fff" stroke-width="2"/></svg></div>

<!-- hero -->
<section class="abs hero" role="img" aria-label="Photo of a young caregiver embracing a smiling elderly woman at home">
  <h1 class="serif">Providing<br><em>Care</em> at home<br>for people</h1>
  <div class="sub">WITH DISABILITY AND THE ELDERLY</div>
  <div class="btn blue" style="left:92px;top:378px;width:289px;height:52px">Make an appointment <span class="dot"></span></div>
  <div class="arrow-side" style="left:0;top:195px">&#8249;</div>
  <div class="arrow-side" style="left:1163px;top:195px">&#8250;</div>
  <svg class="abs" style="left:0;top:470px" width="1200" height="120" viewBox="0 0 1200 120" preserveAspectRatio="none"><polygon points="0,120 1200,0 1200,120" fill="#e6e6e6"/><polygon points="0,120 1200,22 1200,120" fill="#fff"/></svg>
</section>

<!-- about -->
<div class="abs about-art" role="img" aria-label="Ornamental frame around the company emblem"><div class="core">MAPLECREST</div></div>
<div class="abs" style="left:633px;top:793px;width:480px">
  <div class="eyebrow">ABOUT US</div>
  <h2 class="serif" style="font-size:38px;line-height:52px;margin-top:12px">A simple, smart<br>home care</h2>
  <p class="body" style="margin-top:16px">Lorem ipsum dolor sit amet consectetur adipisc elitor sed do eiusmod tempor incididunt ut labore et nisidi dolore magna aliqua. Quis ipsum suspendisse suppu ultrices gravida. Risus commodo viverra maecen eds accumsan lacus vel facilisis.</p>
</div>
<div class="btn green" style="left:633px;top:1120px;width:223px;height:49px">More about us <span class="dot"></span></div>

<!-- features -->
<div class="feature" style="left:82px">
  <div class="icon"><i><svg width="60" height="60" viewBox="0 0 60 60" fill="none" stroke="#fff" stroke-width="2.5"><path d="M30 30c-8-6-12-10-12-15a6 6 0 0 1 12-1 6 6 0 0 1 12 1c0 5-4 9-12 15z"/><path d="M6 30v14l12 10M54 30v14L42 54"/></svg></i></div>
  <h3 class="serif">Professional &amp;<br>friendly staff</h3>
  <p>Lorem ipsum dolor sit amet to consectetur adipisicing elit sed do eiusmod tempor incidid.</p>
</div>
<div class="feature" style="left:448px">
  <div class="icon"><i><svg width="60" height="60" viewBox="0 0 60 60" fill="none" stroke="#fff" stroke-width="2.5"><rect x="14" y="10" width="32" height="42" rx="3"/><rect x="23" y="6" width="14" height="8" rx="2"/><path d="M20 24l3 3 5-5M32 25h8M20 36l3 3 5-5M32 37h8"/></svg></i></div>
  <h3 class="serif">Free in home<br>assessments</h3>
  <p>Lorem ipsum dolor sit amet to consectetur adipisicing elit sed do eiusmod tempor incidid.</p>
</div>
<div class="feature" style="left:812px">
  <div class="icon"><i><svg width="60" height="60" viewBox="0 0 60 60" fill="none" stroke="#fff" stroke-width="2.5"><circle cx="20" cy="16" r="6"/><circle cx="40" cy="16" r="6"/><path d="M10 52V32a10 10 0 0 1 20 0v20M30 52V32a10 10 0 0 1 20 0v20"/></svg></i></div>
  <h3 class="serif">24/7<br>carefull team</h3>
  <p>Lorem ipsum dolor sit amet to consectetur adipisicing elit sed do eiusmod tempor incidid.</p>
</div>
<svg class="abs" style="left:345px;top:1395px" width="150" height="40"><path d="M5 10 Q70 40 140 25" stroke="var(--green)" stroke-width="2" stroke-dasharray="5 5" fill="none"/><path d="M132 20l9 5-7 6" stroke="var(--green)" stroke-width="2" fill="none"/></svg>
<svg class="abs" style="left:712px;top:1395px" width="150" height="40"><path d="M5 30 Q70 0 140 20" stroke="var(--green)" stroke-width="2" stroke-dasharray="5 5" fill="none"/><path d="M130 14l11 6-8 7" stroke="var(--green)" stroke-width="2" fill="none"/></svg>

<!-- services -->
<div class="abs services-bg"></div>
<div class="abs services-photo" role="img" aria-label="Photo of a nurse caring for an elderly woman"></div>
<h2 class="abs center serif" style="top:1790px;font-size:40px">Our services</h2>
<p class="abs center body" style="top:1840px">Lorem ipsum dolor sit amet consectetur adipisc<br>elitor sed do eiusmod tempor incididunt ut</p>
<div class="card" style="left:92px"><div class="ph" role="img" aria-label="Photo of a caregiver's hand supporting an elderly hand on a cane" style="background:linear-gradient(135deg,#4a4a48,#8a7a6a)"></div><h3 class="serif">Companion care</h3><p>Lorem ipsum dolor sit amet to consectetur adipisicing elit so sed do eiusmod tempor..</p><div class="more">READ MORE</div></div>
<div class="card" style="left:437px"><div class="ph" role="img" aria-label="Photo of a housekeeper holding folded towels" style="background:linear-gradient(135deg,#b59f88,#e8e3dd)"></div><h3 class="serif">Light housekeeping</h3><p>Lorem ipsum dolor sit amet to consectetur adipisicing elit so sed do eiusmod tempor..</p><div class="more">READ MORE</div></div>
<div class="card" style="left:782px"><div class="ph" role="img" aria-label="Photo of a woman cooking a meal in a kitchen" style="background:linear-gradient(135deg,#5e4a3e,#b88f78)"></div><h3 class="serif">Meal preparation</h3><p>Lorem ipsum dolor sit amet to consectetur adipisicing elit so sed do eiusmod tempor..</p><div class="more">READ MORE</div></div>
<div class="green-arrow" style="left:92px;top:2027px">&#8249;</div>
<div class="green-arrow" style="left:1070px;top:2027px">&#8250;</div>
<div class="btn green" style="left:482px;top:2473px;width:237px;height:49px">View all service <span class="dot"></span></div>

<!-- testimonials -->
<div class="abs" style="left:578px;top:2587px;width:44px;height:44px;border-radius:50%;border:3px solid var(--blue)"></div>
<h2 class="abs center serif" style="top:2638px;font-size:40px">Client testimonials</h2>
<p class="abs center body" style="top:2688px">Lorem ipsum dolor sit amet consectetur adipisc elitor<br>sed do eiusmod tempor incididunt ut</p>
<div class="abs quote-pill"></div>
<svg class="abs" style="left:155px;top:2788px" width="330" height="370" viewBox="0 0 330 370"><path d="M162 0a158 158 0 0 1 90 288L225 362 188 316A158 158 0 1 1 162 0z" fill="#d9dadc"/></svg>
<div class="abs" style="left:162px;top:2795px;width:310px;height:310px;border-radius:50%;background:linear-gradient(160deg,#c9cbcf,#6f7377 70%,#2e2f31)" role="img" aria-label="Portrait photo of a smiling client wearing glasses"></div>
<div class="abs serif" style="left:405px;top:2840px;font-size:90px;color:#fff;line-height:1">&rdquo;</div>
<div class="abs" style="left:503px;top:2895px;width:2px;height:170px;background:#6a6d6e"></div>
<div class="abs quote-text">Lorem ipsum dolor sit amet, consectetur adipisici elit sed do eiusmod tempor incididunt ut labore et se dolore magna aliqua. Ut enim ad minim venia quis nostrud exercitation ullamco laboris nisi
  <div class="serif" style="font-style:normal;color:#fff;font-size:19px;margin-top:12px">Daniel Whitford</div>
  <div class="stars"><svg width="110" height="18" viewBox="0 0 110 18" fill="#f5c518"><path id="s" d="M9 0l2.6 6 6.4.5-4.9 4.2 1.5 6.3L9 13.6 3.4 17l1.5-6.3L0 6.5 6.4 6z"/><use href="#s" x="23"/><use href="#s" x="46"/><use href="#s" x="69"/><use href="#s" x="92"/></svg></div>
</div>
<div class="green-arrow" style="left:92px;top:2940px">&#8249;</div>
<div class="green-arrow" style="left:1070px;top:2940px">&#8250;</div>

<!-- contact -->
<section class="abs contact" role="img" aria-label="Blue-tinted photo of a caregiver holding a patient's hands">
  <h2 class="abs center serif" style="top:68px;font-size:40px;color:#fff">Contact us</h2>
  <p class="abs center body" style="top:118px;color:#fff">Lorem ipsum dolor sit amet consectetur adipisc elitor<br>sed do eiusmod tempor incididunt ut</p>
  <div class="field" style="left:242px;top:231px;width:351px;height:47px">Your Name</div>
  <div class="field" style="left:242px;top:293px;width:351px;height:47px">Email Address</div>
  <div class="field" style="left:242px;top:356px;width:351px;height:47px">Phone No</div>
  <div class="field" style="left:607px;top:231px;width:353px;height:174px">Leave your message</div>
  <div class="btn green" style="left:502px;top:425px;width:196px;height:46px">Submit now <span class="dot"></span></div>
</section>

<!-- footer -->
<footer class="abs footer">
  <svg class="abs" style="left:0;top:-1px" width="1200" height="130" viewBox="0 0 1200 130" preserveAspectRatio="none"><polygon points="0,0 1200,0 1200,110 0,0" fill="#125b8d"/><polygon points="300,30 1200,110 1200,130" fill="#e6e6e6"/></svg>
  <div class="abs" style="left:92px;top:170px;display:flex;align-items:center;gap:14px"><span style="width:80px;height:80px;border-radius:50%;background:var(--blue)"></span><span class="serif" style="color:var(--blue);font-size:30px;line-height:1.1">Maplecrest<br><span style="font-family:Montserrat,sans-serif;font-weight:500;font-size:12px;letter-spacing:6px">HOME CARE</span></span></div>
  <p class="abs body" style="left:92px;top:258px;width:390px;color:#ddd">Lorem ipsum dolor sit amet consectetur sei adipisicing elit sed do eiusmod tempor esd incididunt ut labore et dolore magna qualit aliqua. Ut enim ad minim veniam.</p>
  <div class="abs" style="left:567px;top:150px"><h4 class="serif">Quick links</h4><div class="links" style="margin-top:12px">Home<br>About<br>Services<br>Resources<br>Contact</div></div>
  <div class="abs" style="left:822px;top:150px;width:300px"><h4 class="serif" style="margin-bottom:26px">Contact info</h4>
    <div class="ci"><span class="c"><svg width="16" height="20" viewBox="0 0 16 20" fill="#fff"><path d="M8 0a8 8 0 0 1 8 8c0 6-8 12-8 12S0 14 0 8a8 8 0 0 1 8-8z"/><circle cx="8" cy="8" r="3" fill="#5b9a3a"/></svg></span><span>enim admin minim veniam nostrud exercitation</span></div>
    <div class="ci"><span class="c"><svg width="18" height="18" viewBox="0 0 24 24" fill="#fff"><path d="M6.6 10.8a15 15 0 0 0 6.6 6.6l2.2-2.2c.3-.3.7-.4 1-.2 1.1.4 2.3.6 3.6.6.6 0 1 .4 1 1V20c0 .6-.4 1-1 1A17 17 0 0 1 3 4c0-.6.4-1 1-1h3.5c.6 0 1 .4 1 1 0 1.3.2 2.5.6 3.6.1.3 0 .7-.2 1z"/></svg></span><span>Call Us:<br>555-218-4630</span></div>
    <div class="ci"><span class="c"><svg width="18" height="16" viewBox="0 0 24 20" fill="#fff"><rect x="1" y="2" width="22" height="16" rx="2"/><path d="M2 4l10 7 10-7" stroke="#5b9a3a" stroke-width="2" fill="none"/></svg></span><span>Mail Us:<br>info@maplecresthome.com</span></div>
  </div>
  <div class="abs" style="left:92px;top:455px;font-size:15px;color:#888">Copyright © 2022 Maplecrest Home Care. All rights reserved.</div>
  <div class="abs" style="left:905px;top:443px;display:flex;gap:13px"><span class="social"></span><span class="social"></span><span class="social"></span><span class="social"></span></div>
</footer>

</body>
</html>
```